Vell Expertline home page

I want a new look and design for the home page of www.vellexpertline.example . Something new that better shows what our service is about. We provide live technical support to RE professionals via our smart phone app and website. The service is available for home inspectors, appraisers, real estate agents and others in the Real Estate Profession.

I just want a great looking home page design that demonstrates the service. Does not have to be a functional site, just the design.

Imagine walking around or through a house and having a technical question during your inspection. You pull out your phone, open the Vell Exp app and select a category, type in your question and it opens your camera to attach a photo. You submit your question and experts review it and send you an answer within minutes. Possibly while you are still on the job.
Updates

I am really looking for a way to convey that our service is all about RE professionals, like home inspectors, appraisers, RE agents getting help while they are in the field at the homes they are working at.   A home inspector looks at an electrical panel snaps a picture and sends their question to us and they get a response before they even leave the jobsite.  That feeling.

Reason: I would like to see the designs convey the feeling that our service is something every professional needs while doing their jobs. We have hundreds of inspectors using our service to get fast answers to very technical questions using our smart phone app.

Target Market(s)

Home Inspectors, Real Estate Appraisers, Real Estate Agents

Industry/Entity Type

Real Estate

Colors

Designer to choose colors to be used in the design.

Requirements
Must have
• People must understand we provide experts who respond to their real estate related technical support questions using our patent pending smart phone app.

```html
<!DOCTYPE html>
<html lang="en">
<head>
<meta charset="utf-8">
<title>Vell Expertline — Live Technical Support for Real Estate Professionals</title>
<link href="https://fonts.googleapis.com/css2?family=Open+Sans:wght@400;600;700&display=swap" rel="stylesheet">
<style>
:root{
  --red:#e3121b;
  --black:#111111;
  --ink:#333333;
  --muted:#777777;
  --line:#dddddd;
  --footer:#1d1d1d;
  --footer-text:#9a9a9a;
  --white:#ffffff;
}
*{box-sizing:border-box;margin:0;padding:0}
html,body{width:891px;height:1200px;overflow:hidden}
body{font-family:"Open Sans",Arial,sans-serif;color:var(--ink);background:var(--white);position:relative}

/* Header */
.site-header{position:absolute;top:0;left:0;width:891px;height:84px;background:var(--white);border-bottom:1px solid var(--line)}
.brand{position:absolute;left:30px;top:0;width:120px;height:84px;background:var(--black);display:flex;align-items:center;justify-content:center;gap:6px}
.brand-mark{width:12px;height:12px;background:var(--red)}
.brand-name{color:var(--white);font-weight:700;font-size:13px;line-height:1.1;width:76px}
.top-contact{position:absolute;right:30px;top:8px;font-size:11px;color:var(--red);font-weight:600}
.top-contact span{color:var(--ink);margin-left:6px}
.main-nav{position:absolute;left:285px;right:30px;top:38px;height:34px;background:var(--black);display:flex;align-items:center;padding-left:4px}
.main-nav a{color:var(--white);text-decoration:none;font-size:11.5px;font-weight:600;padding:0 12px;height:34px;line-height:34px}
.main-nav a.active{background:var(--red)}

/* Hero */
.hero{position:absolute;top:85px;left:0;width:891px;height:300px;background:linear-gradient(180deg,#ffffff 0%,#eeeeee 100%);border-bottom:3px solid var(--red)}
.hero-copy{position:absolute;left:60px;top:28px;width:430px}
.hero-kicker{font-size:20px;color:var(--muted)}
.hero-call{font-size:34px;line-height:1.15;color:var(--red);margin-top:2px}
.hero-call strong{color:var(--black);font-weight:700}
.hero-note{font-size:9px;color:var(--muted);margin-top:10px}
.hero-plans{font-size:13px;color:var(--muted);margin-top:42px}
.hero-app{font-size:16px;color:var(--red);font-weight:600}
.phone-visual{position:absolute;left:560px;top:18px;width:200px;height:250px;border-radius:26px;background:linear-gradient(160deg,#3a3a3a 0%,#0d0d0d 100%)}
.store-badges{position:absolute;left:600px;top:244px;display:flex;gap:8px}
.store-badge{width:84px;height:26px;border-radius:4px;background:#444}
.store-badge.green{background:#6aa536}

/* Sections */
.section-title{text-align:center;font-size:21px;color:var(--ink);font-weight:400}
.section-title b{font-weight:600}
.title-rule{width:60px;height:2px;background:var(--red);margin:8px auto 0}

.features{position:absolute;top:412px;left:0;width:891px}
.feature-grid{display:grid;grid-template-columns:repeat(6,1fr);row-gap:22px;width:780px;margin:26px auto 0}
.feature{text-align:center}
.feature-icon{width:52px;height:52px;border-radius:10px;background:var(--black);margin:0 auto;display:flex;align-items:center;justify-content:center}
.feature-icon svg{width:26px;height:26px;fill:none;stroke:var(--white);stroke-width:2;stroke-linecap:round;stroke-linejoin:round}
.feature-label{font-size:10px;color:var(--ink);margin-top:7px}

.services{position:absolute;top:700px;left:0;width:891px}
.service-grid{display:grid;grid-template-columns:repeat(3,1fr);gap:34px;width:800px;margin:26px auto 0}
.service-head{display:flex;align-items:flex-start;gap:10px}
.service-photo{width:110px;height:100px;background:linear-gradient(160deg,#d9c9b4,#8d7a66)}
.service-photo.appraiser{background:linear-gradient(160deg,#cfd6de,#4a5563)}
.service-photo.realestate{background:linear-gradient(160deg,#c9d9c0,#7c8f6e)}
.service-name{font-size:13px;font-weight:600;color:var(--black);margin-top:6px}
.service-text{font-size:9.5px;line-height:1.45;color:var(--muted);margin-top:10px}
.btn{display:inline-block;background:var(--red);color:var(--white);font-size:10px;font-weight:600;padding:5px 12px;border-radius:3px;margin-top:10px;text-decoration:none}

/* Footer */
.site-footer{position:absolute;top:985px;left:0;width:891px;height:215px;background:var(--footer)}
.footer-cols{display:grid;grid-template-columns:1fr 1fr 1.3fr 1fr;width:800px;margin:0 auto;padding-top:18px}
.footer-title{color:var(--red);font-size:11px;font-weight:700;margin-bottom:8px}
.footer-list{list-style:none}
.footer-list li{font-size:9px;color:var(--footer-text);line-height:1.7}
.footer-note{font-size:9px;color:var(--footer-text);line-height:1.5;width:190px}
.signup{display:flex;margin-top:8px}
.signup-input{width:110px;height:18px;background:var(--white)}
.signup-btn{background:var(--red);color:var(--white);font-size:9px;font-weight:600;padding:0 10px;line-height:18px}
.social li{display:flex;align-items:center;gap:8px;margin-bottom:6px}
.social-dot{width:14px;height:14px;border-radius:50%;background:#555}
.copyright{position:absolute;bottom:0;left:0;width:100%;height:24px;background:var(--black);color:var(--footer-text);font-size:9px;text-align:center;line-height:24px}
</style>
</head>
<body>

<header class="site-header">
  <div class="brand"><span class="brand-mark"></span><span class="brand-name">Vell Expertline</span></div>
  <div class="top-contact">Call Dana Whitlock at 555-014-2290 <span>| Login</span></div>
  <nav class="main-nav">
    <a class="active" href="#">Home</a><a href="#">Membership</a><a href="#">Features</a><a href="#">About Us</a><a href="#">Plan Comparison</a><a href="#">FAQ's</a><a href="#">Contact Us</a>
  </nav>
</header>

<section class="hero">
  <div class="hero-copy">
    <p class="hero-kicker">Find out how to join for FREE today!</p>
    <p class="hero-call">Call <strong>Dana Whitlock</strong> at<br><strong>555-014-2290</strong> for more information</p>
    <p class="hero-note">*Benefits vary depending on your membership level and plan. See website for details.</p>
    <p class="hero-plans">Premier, Premier-Plus, Elite and Corporate memberships available</p>
    <p class="hero-app">Vell Exp Support App on your smartphone!</p>
  </div>
  <div class="phone-visual" role="img" aria-label="Smartphone showing the Vell Exp support app start screen"></div>
  <div class="store-badges"><span class="store-badge"></span><span class="store-badge"></span><span class="store-badge green"></span></div>
</section>

<section class="features">
  <h2 class="section-title">Features <b>Of Our App</b></h2>
  <div class="title-rule"></div>
  <div class="feature-grid">
    <div class="feature"><div class="feature-icon"><svg viewBox="0 0 24 24"><path d="M4 14v-2a8 8 0 0 1 16 0v2"/><rect x="3" y="14" width="4" height="6"/><rect x="17" y="14" width="4" height="6"/></svg></div><p class="feature-label">Technical Support</p></div>
    <div class="feature"><div class="feature-icon"><svg viewBox="0 0 24 24"><path d="M12 3l9 16H3z"/><path d="M12 10v4M12 17v.5"/></svg></div><p class="feature-label">Risk Assessment Tools</p></div>
    <div class="feature"><div class="feature-icon"><svg viewBox="0 0 24 24"><path d="M5 4h10l4 4v12H5z"/><path d="M8 12h8M8 16h8"/></svg></div><p class="feature-label">Professional Resources</p></div>
    <div class="feature"><div class="feature-icon"><svg viewBox="0 0 24 24"><path d="M2 9l10-5 10 5-10 5z"/><path d="M6 11v5c3 2 9 2 12 0v-5"/></svg></div><p class="feature-label">Education</p></div>
    <div class="feature"><div class="feature-icon"><svg viewBox="0 0 24 24"><path d="M4 20V14M10 20V10M16 20V6"/><path d="M3 11l6-5 4 3 7-6"/></svg></div><p class="feature-label">Business Growth</p></div>
    <div class="feature"><div class="feature-icon"><svg viewBox="0 0 24 24"><path d="M3 5h18v11H9l-5 4V5z"/><path d="M9 9h6M9 12h4"/></svg></div><p class="feature-label">Member Q&amp;A</p></div>
    <div class="feature"><div class="feature-icon"><svg viewBox="0 0 24 24"><rect x="3" y="6" width="18" height="12"/><path d="M3 6l9 7 9-7"/></svg></div><p class="feature-label">E-Newsletter</p></div>
    <div class="feature"><div class="feature-icon"><svg viewBox="0 0 24 24"><path d="M3 12l9-9h8v8l-9 9z"/><circle cx="16" cy="8" r="1.5"/></svg></div><p class="feature-label">Vendor Discounts</p></div>
    <div class="feature"><div class="feature-icon"><svg viewBox="0 0 24 24"><path d="M12 3v18M5 21h14M4 7h16"/><path d="M4 7l-2 6h6zM20 7l-2 6h6z"/></svg></div><p class="feature-label">Consult Attorney</p></div>
    <div class="feature"><div class="feature-icon"><svg viewBox="0 0 24 24"><circle cx="8" cy="8" r="3"/><circle cx="16" cy="8" r="3"/><path d="M2 20c0-4 3-6 6-6s6 2 6 6M12 16c1-1 2-2 4-2 3 0 6 2 6 6"/></svg></div><p class="feature-label">Professional Forums</p></div>
    <div class="feature"><div class="feature-icon"><svg viewBox="0 0 24 24"><path d="M3 4h3l3 12h10l2-8H7"/><circle cx="10" cy="20" r="1.5"/><circle cx="17" cy="20" r="1.5"/></svg></div><p class="feature-label">Products Discounts</p></div>
    <div class="feature"><div class="feature-icon"><svg viewBox="0 0 24 24"><rect x="3" y="4" width="18" height="12"/><path d="M12 16v4M8 20h8"/></svg></div><p class="feature-label">Professional Conference</p></div>
  </div>
</section>

<section class="services">
  <h2 class="section-title">Services <b>Of Our App</b></h2>
  <div class="title-rule"></div>
  <div class="service-grid">
    <article class="service">
      <div class="service-head"><div class="service-photo" role="img" aria-label="Home inspector checking a house on site"></div><h3 class="service-name">Home Inspectors</h3></div>
      <p class="service-text">Snap a photo of a panel, roof or furnace and send your question from the job. Our experts reply within minutes, often before you leave the site.</p>
      <a class="btn" href="#">Read More</a>
    </article>
    <article class="service">
      <div class="service-head"><div class="service-photo appraiser" role="img" aria-label="Appraiser reviewing a property report"></div><h3 class="service-name">Appraisers</h3></div>
      <p class="service-text">Get quick answers on construction details, materials and defects while you walk the property, so every report you file is backed by experts.</p>
      <a class="btn" href="#">Read More</a>
    </article>
    <article class="service">
      <div class="service-head"><div class="service-photo realestate" role="img" aria-label="Real estate agent in front of a home for sale"></div><h3 class="service-name">Real Estate</h3></div>
      <p class="service-text">Agents can ask about any issue found at a showing and share clear expert answers with buyers and sellers the same day, right from the app.</p>
      <a class="btn" href="#">Read More</a>
    </article>
  </div>
</section>

<footer class="site-footer">
  <div class="footer-cols">
    <div>
      <h4 class="footer-title">Quick Links</h4>
      <ul class="footer-list"><li>Home</li><li>About Us</li><li>Services</li><li>Service Plans</li><li>News</li><li>FAQ &amp; Help</li><li>Contact</li></ul>
    </div>
    <div>
      <h4 class="footer-title">Support Links</h4>
      <ul class="footer-list"><li>Legal Notice</li><li>Privacy Policy</li><li>Terms &amp; Conditions</li><li>Help</li></ul>
    </div>
    <div>
      <h4 class="footer-title">Newsletter Signup</h4>
      <p class="footer-note">Sign up for our news and tips by entering your email address below.</p>
      <div class="signup"><span class="signup-input"></span><span class="signup-btn">Subscribe</span></div>
    </div>
    <div>
      <h4 class="footer-title">Connect With Us</h4>
      <ul class="footer-list social"><li><span class="social-dot"></span>News Feed</li><li><span class="social-dot"></span>Community Page</li><li><span class="social-dot"></span>Pro Network</li></ul>
    </div>
  </div>
  <div class="copyright">Copyright ©2015 Vell Expertline - All rights reserved</div>
</footer>

</body>
</html>
```